Start up in business consultancy needs a business card

We need the business card's layout (we have already the logo). Our business is concerned on consultancy services delivered to companies on the matter of sustainability. Business card should be enough essentials and professional style.

Side A with the following info:
logo + a space for the claim (still to identify) + website of the company

Side B with the following info:
Name of business card holder + title of the business card holder + address of the company + space for mobile number, phone number, fax number + e-mail of business card holder + graphic details around.

Target Market(s)

Business of any sector

Industry/Entity Type

Business Service

Contact Information for Business Card

Name of the company:
Pianoverde srl
Società Benefit

Address of the company:
Via Lucerna, 7
21047 - Saronno (VA)

Website:
www.pianoverde.it

Name of the BC' holder:
Luca Ferentino

Title:
Co-fondatore

Email:
luca@pianoverde.it

Mobile:
+39 348 915 2074
Phone:
+39 348 915 2074
Fax:
+39 348 915 2074

Font styles to use
Other font styles liked:
• new gothic

```html
<!DOCTYPE html>
<html lang="it">
<head>
<meta charset="UTF-8">
<title>Pianoverde – biglietto da visita</title>
<link href="https://fonts.googleapis.com/css2?family=Archivo:wght@400;600;800&display=swap" rel="stylesheet">
<style>
  :root {
    --brand-blue: #0061a8;
    --paper: #f4f5f8;
    --ink: #2b2b2f;
    --edge-grey: #8d8f94;
    --backdrop: #e2e1ec;
  }
  * { box-sizing: border-box; margin: 0; padding: 0; }
  html, body {
    width: 1200px; height: 906px; overflow: hidden;
    background: var(--backdrop);
    font-family: "Archivo", Arial, sans-serif;
  }
  .sheet {
    width: 1200px; height: 906px;
    display: flex; flex-direction: column; align-items: center; justify-content: center;
    gap: 40px;
  }
  .card {
    position: relative;
    width: 600px; height: 388px;
    box-shadow: 0 10px 28px rgba(40, 40, 80, 0.18);
    overflow: hidden;
  }

  /* Side A */
  .card--front { background: var(--brand-blue); color: #fff; }
  .brand {
    display: flex; align-items: center; gap: 14px;
  }
  .brand__mark {
    width: 62px; height: 62px; border-radius: 50%;
    border: 3px solid currentColor; flex: none;
  }
  .brand__name { font-weight: 600; font-size: 40px; letter-spacing: 0.5px; line-height: 1; }
  .card--front .brand {
    position: absolute; top: 150px; left: 50%; transform: translateX(-50%);
  }
  .card--front .website {
    position: absolute; bottom: 52px; left: 0; right: 0;
    text-align: center; font-size: 14px; letter-spacing: 0.6px;
  }

  /* Side B */
  .card--back { background: var(--paper); color: var(--ink); }
  .card--back .brand {
    position: absolute; top: 62px; right: 44px; color: var(--brand-blue);
  }
  .card--back .brand__mark { width: 58px; height: 58px; }
  .card--back .brand__name { font-size: 32px; }

  .holder { position: absolute; top: 176px; left: 54px; }
  .holder__name {
    color: var(--brand-blue); font-weight: 800; font-size: 21px;
    text-transform: uppercase; letter-spacing: 0.2px;
  }
  .holder__role { font-size: 16px; margin-top: 4px; }

  .contacts {
    position: absolute; top: 262px; left: 72px;
    list-style: none; font-size: 14px; line-height: 21px;
  }
  .contacts li { display: flex; align-items: center; gap: 9px; }
  .contacts svg { width: 14px; height: 14px; flex: none; fill: var(--brand-blue); }

  .company {
    position: absolute; top: 196px; right: 44px;
    text-align: right; font-size: 14px; line-height: 19px;
  }
  .company__name {
    color: var(--brand-blue); font-weight: 800; text-transform: uppercase; font-size: 14px;
  }

  .edge-band { position: absolute; left: 0; bottom: 0; width: 600px; height: 12px; }
</style>
</head>
<body>
<main class="sheet">

  <section class="card card--front" aria-label="Fronte">
    <div class="brand">
      <span class="brand__mark"></span>
      <span class="brand__name">pianoverde</span>
    </div>
    <p class="website">www.pianoverde.it</p>
  </section>

  <section class="card card--back" aria-label="Retro">
    <div class="brand">
      <span class="brand__mark"></span>
      <span class="brand__name">pianoverde</span>
    </div>

    <div class="holder">
      <h1 class="holder__name">Luca Ferentino</h1>
      <p class="holder__role">Co-fondatore</p>
    </div>

    <address class="company" style="font-style:normal">
      <div class="company__name">Pianoverde srl</div>
      <div>Via Lucerna, 7</div>
      <div>21047 - Saronno (VA)</div>
    </address>

    <ul class="contacts">
      <li>
        <svg viewBox="0 0 14 14" aria-label="Cellulare"><path d="M4 1h6a1 1 0 0 1 1 1v10a1 1 0 0 1-1 1H4a1 1 0 0 1-1-1V2a1 1 0 0 1 1-1zm.5 1.5v8h5v-8z"/></svg>
        +39 348 915 2074
      </li>
      <li>
        <svg viewBox="0 0 14 14" aria-label="Telefono"><path d="M3 1l2.4 2.6-1.3 1.6c.8 1.8 2.1 3.1 3.9 3.9l1.6-1.3L12 10.2 10.6 12.6C6 12.3 1.7 8 1.4 3.4z"/></svg>
        +39 348 915 2074
      </li>
      <li>
        <svg viewBox="0 0 14 14" aria-label="E-mail"><path d="M1 3h12v8H1zm1.3 1L7 7.6 11.7 4zM2 5v5h10V5L7 8.9z"/></svg>
        luca@pianoverde.it
      </li>
      <li>
        <svg viewBox="0 0 14 14" aria-label="Sito web"><path d="M7 1a6 6 0 1 0 0 12A6 6 0 0 0 7 1zm0 1.2c.8.8 1.3 2.1 1.5 3.3h-3C5.7 4.3 6.2 3 7 2.2zM2.3 6.5h2.1c0 1 .2 2 .5 2.9H3a4.8 4.8 0 0 1-.7-2.9zm0-1a4.8 4.8 0 0 1 .7-1.9h1.9c-.3.6-.4 1.2-.5 1.9zm3.2 1h3c0 1-.2 2-.5 2.9h-2c-.3-.9-.5-1.9-.5-2.9zm4.1 0h2.1a4.8 4.8 0 0 1-.7 2.9H9.1c.3-.9.5-1.9.5-2.9zm2.1-1H9.6c-.1-.7-.2-1.3-.5-1.9H11c.4.6.6 1.2.7 1.9zM7 11.8c-.5-.5-.9-1.2-1.2-2.1h2.4c-.3.9-.7 1.6-1.2 2.1z"/></svg>
        www.pianoverde.it
      </li>
    </ul>

    <svg class="edge-band" viewBox="0 0 600 12" preserveAspectRatio="none" aria-hidden="true">
      <polygon points="0,4 392,4 384,12 0,12" fill="var(--edge-grey)"/>
      <polygon points="400,0 600,0 600,12 388,12" fill="var(--brand-blue)"/>
    </svg>
  </section>

</main>
</body>
</html>
```